Conservative, Modern and Sharp Builder Business card

Hi there,
We would like to update our existing business card.
I have attached photos of existing business card, logo and van sign.

I would like the business card to also list what we do :
Renovation • New Build • Alteration
Extension • Bathroom • Maintenance.(Seperated by dots)

Contact number : 021 0483 0752
(With that exact spacing)

Ideally when people looking from about 2-3 metres, they know that it is a builder’s business card

Open to suggestions on fonts, layout, style of business card

PLEASE ONLY SUBMIT YOUR BEST OR MAX 3 DESIGNS FOR EACH DESIGNER

Thanks

Construction. Renovation

Details should be the same as the existing card. And addition of what we do.

• The new business card must not have the same layout as our existing one. Thanks

```html
<!DOCTYPE html>
<html lang="en">
<head>
<meta charset="utf-8">
<title>Stonefield Build – Business Card</title>
<link rel="stylesheet" href="https://fonts.googleapis.com/css2?family=Open+Sans:wght@400;600;700&display=swap">
<style>
  :root{
    --backdrop:#e6e2dd;
    --card:#25262a;
    --card-deep:#1c1d20;
    --card-deeper:#151619;
    --pattern-a:#2c2d31;
    --pattern-b:#222326;
    --ink:#ffffff;
    --ink-soft:#f1f1f1;
  }
  *{margin:0;padding:0;box-sizing:border-box}
  html,body{width:1200px;height:780px;overflow:hidden}
  body{background:var(--backdrop);font-family:"Open Sans",Arial,sans-serif;position:relative}
  .card{position:absolute;top:70px;width:367px;height:642px;border-radius:24px;overflow:hidden;background:var(--card);box-shadow:0 10px 24px rgba(0,0,0,.25)}
  .card--back{left:208px}
  .card--front{left:625px}

  .brand-pattern{position:absolute;inset:0;background:linear-gradient(160deg,var(--pattern-a),var(--pattern-b))}
  .back-mark{position:absolute;left:218px;top:552px;width:120px;text-align:center;color:var(--ink);font-weight:700;font-size:13px;line-height:1.15}
  .back-mark .mark-square{display:block;width:12px;height:12px;background:var(--ink);margin:0 auto 5px}

  .front-waves{position:absolute;left:0;top:0;width:367px;height:642px}
  .brand{position:absolute;top:40px;left:0;width:100%;text-align:center;color:var(--ink)}
  .brand .mark-square{display:block;width:44px;height:44px;background:var(--ink);margin:0 auto 22px}
  .brand-name{font-weight:700;font-size:38px;letter-spacing:-.5px;line-height:1}

  .person{position:absolute;top:232px;width:100%;text-align:center;color:var(--ink)}
  .person-name{font-weight:700;font-size:32px;line-height:1.1}
  .person-role{font-weight:600;font-size:17px;margin-top:6px}

  .contacts{position:absolute;top:328px;width:100%;list-style:none;color:var(--ink-soft);font-size:17px;line-height:25.5px}
  .contacts li{display:flex;justify-content:center;align-items:center;gap:7px}
  .contacts svg{width:15px;height:15px;flex:none}

  .services{position:absolute;top:562px;width:100%;text-align:center;color:var(--ink-soft);font-size:16px;line-height:24px}
</style>
</head>
<body>
  <section class="card card--back" aria-label="Card back">
    <div class="brand-pattern" role="img" aria-label="Repeating embossed brand-mark pattern in dark grey"></div>
    <div class="back-mark"><span class="mark-square"></span>Stonefield Build</div>
  </section>

  <section class="card card--front" aria-label="Card front">
    <svg class="front-waves" viewBox="0 0 367 642" aria-hidden="true">
      <path d="M0 408 Q120 470 367 410 L367 642 L0 642 Z" fill="#202124"/>
      <path d="M0 408 Q60 460 180 468 Q300 470 367 410 L367 518 Q200 540 170 508 Q120 525 0 545 Z" fill="var(--card-deeper)" opacity=".8"/>
      <path d="M0 545 Q120 525 170 508 Q220 530 367 518 L367 642 L0 642 Z" fill="var(--card)"/>
    </svg>

    <div class="brand">
      <span class="mark-square"></span>
      <div class="brand-name">Stonefield Build</div>
    </div>

    <div class="person">
      <div class="person-name">Tomas Verhoeven</div>
      <div class="person-role">Residential Builder</div>
    </div>

    <ul class="contacts">
      <li><svg viewBox="0 0 24 24"><path fill="#fff" d="M6.6 10.8a15.1 15.1 0 0 0 6.6 6.6l2.2-2.2a1 1 0 0 1 1-.25 11.4 11.4 0 0 0 3.6.57 1 1 0 0 1 1 1V20a1 1 0 0 1-1 1A17 17 0 0 1 3 4a1 1 0 0 1 1-1h3.5a1 1 0 0 1 1 1c0 1.25.2 2.45.57 3.57a1 1 0 0 1-.25 1z"/></svg>021 0483 0752</li>
      <li><svg viewBox="0 0 24 24"><circle cx="12" cy="12" r="9" fill="none" stroke="#fff" stroke-width="2.4"/></svg>StonefieldBuild.nz</li>
      <li><svg viewBox="0 0 24 24"><circle cx="12" cy="12" r="9.5" fill="none" stroke="#fff" stroke-width="2"/><ellipse cx="12" cy="12" rx="4" ry="9.5" fill="none" stroke="#fff" stroke-width="1.6"/><path d="M2.5 12h19" stroke="#fff" stroke-width="1.6"/></svg>www.StonefieldBuild.co.nz</li>
      <li><svg viewBox="0 0 24 24"><rect x="2.5" y="5" width="19" height="14" rx="1.5" fill="none" stroke="#fff" stroke-width="2"/><path d="M3 6l9 7 9-7" fill="none" stroke="#fff" stroke-width="2"/></svg>hello@stonefieldbuild.co.nz</li>
    </ul>

    <p class="services">Renovations • New Builds • Alterations<br>Extensions • Bathrooms • Maintenances</p>
  </section>
</body>
</html>
```